依頼詳細
明照宗若人会主催「静の語らい」でありますが、ヨーガやマインドフルネスの講師(認知心理学や脳科学の専門家)も来られるためアナログとデジタルの融合のようなチラシだと面白いなと考えています。

禅は一円相(筆の円の一筆書き)のイメージもあるため、表紙に大きめにデジタルで一円相をお願いしたいです。
可能でしたら一円相の中に坐禅している人物のシルエットなど入っているとさらに良いかなと考えています。

表紙は「静の語らい」タイトルやサブタイトル、講師陣のプロフィールや写真を掲載

裏面には詳細なタイムスケジュールや申込み方法、会場への生き方や送迎のご案内などを掲載をお願いします。

以下チラシの表紙裏面の記載事項です。
〈〉ヤマカッコ内は記載でお願いしたいことや希望の配置やフォントの大きさやなどについて記させていただきます。ご了承ください。

〈※表紙に記載事項〉
愛知県東部若人会主催 第52回       〈フォント小さく〉
静の語らい                  〈フォント大きく分かりやすく〉
ヨーガ×マインドフルネス×坐禅         〈分かりやすく〉

〜深い呼吸で身体と心を調える(調身調息調心)〈サブタイトル〉

日時 令和5年 11月18日(土)13時〜16時半 (12時半開場)
場所 慶雲山 桂林院

〈講師のプロフィール〉
古層のヨーガ講座  講師 堀越達也氏

堀越達也(サティヤ・ヨーガ主宰)     〈写真と共にプロフィール掲載〉

『禅の源流である呼吸を中心に身体と息を調える「古層のヨーガ」を伝える。
新潟・浄泉寺、大阪・瑞徳安楽寺、広島・清岸寺、島根・鶴林寺等でヨーガ指導を行う。
2019年 松井道元老師より推奨を受ける。
「サティヤ・ヨーガは、古層のヨーガの姿を彷彿とさせてくれる。
的確なタイミングと表現でかけられる言葉に導かれて動いていく<からだ・息・こころ>。
そして、行き着いたところは坐禅が生まれたところだった。
奥行きのあるヨーガの世界を味わいたい人すべてにお勧めする。」
松井道元・記
アーナンダ・ヨーガHP
https://s-satyayoga.example/ 』

マインドフルネス講座  講師 柴崎和久氏  〈写真と共にプロフィール掲載〉

『港陽大学経営学部卒業後に、医療機器メーカーに7年間勤務し、経営企画管理業務に従事。海外駐在員時代に、10日間のヴィパッサナー瞑想リトリートに参加し、瞑想が身心を健康にすることを体験的に理解し、「働いている場合ではない」と退社。洛北大学教育学部に編入学し、学士・修士・博士を経て、現在に至る。現在は、瞑想の実践者かつ研究者として、瞑想実践を通じてでてきた問いをもとに、認知心理学的手法やMRIなどの実験装置を用いて、瞑想の生理・心理・神経メカニズムを解明する研究を進めている。』

〈下に小さく主催 後援を記載〉
主催 愛知県東部明照宗若人会
後援 大本山清涼寺 大本山妙光寺
明照宗本務庁 明照宗愛知県東部本務所 東海報知

〈裏面に記載事項〉
第52回 静の語らい ヨーガ×マインドフルネス×坐禅
〜深い呼吸で身体と心を調える(調身調息調心)

今年の「静の語らい」はヨーガやマインドフルネスの講師をお招きしてのコラボ企画です。
ヨーガやマインドフルネスで身体・呼吸・心を調え、最後に坐禅をしていただきます。

会場 慶雲山 桂林院 〒466−0999 愛知県名古屋市昭和区梅ヶ丘7−4
対象 一般男女 定員30名
参加費 3000円
当日受付にてお支払いください。
服装 動きやすいゆったりしたもの(スカートやベルトのあるものはお控えください)
更衣室あります。
持ち物 敷物(バスタオルなど)

申し込み方法
QRコード、メール、郵送いずれかの方法でお申し込みください。   〈申込みQRコードを掲載してください〉

氏名、ふりがな、住所、電話番号(携帯可)、送迎の要・不要、駐車場の要・不要など
必要事項を記入の上、申込みください。

〒485ー0077
小牧市南原田2785
観音寺内 愛知県東部明照宗若人会事務局
Mailアドレス  tobu-wakodo@meisho-mail.example

※ご不明な点は会場 桂林院、keiunzan.keirin@meisho-mail.exampleまでお問い合わせ下さい。

〈会場への行き方や略図などの掲載をお願いします。簡単に「送迎の詳細」や「会場までの交通手段」を作らせていただきましたが、これをもとに作り変えていただき「送迎の詳細」と「会場までの交通手段」の掲載をお願いします。
桂林院の周辺略地図はカラーとモノクロ2パターンあるので使用していただけるとありがたいです。〉

市バス 柳谷町 徒歩5分
地下鉄
東山線 松林駅 徒歩15分
鶴舞線 桜台駅 徒歩15分
名城線 港陽学園駅 徒歩10分
車 桂林院西駐車場 多数完備
記載項目
〈表紙に記載事項〉
愛知県東部若人会主催 第52回
静の語らい
ヨーガ×マインドフルネス×坐禅

〜深い呼吸で身体と心を調える(調身調息調心)

場所 慶雲山 桂林院

古層のヨーガ 講師 堀越達也氏
マインドフルネス講座  講師 柴崎和久氏

主催 愛知県東部明照宗若人会
後援 大本山清涼寺 大本山妙光寺
明照宗本務庁 明照宗愛知県東部本務所 東海報知

〈裏面に記載事項〉
第52回 静の語らい ヨーガ×マインドフルネス×坐禅

対象 一般男女 定員30名
参加費 3000円
当日受付にてお支払いください。
更衣室あります。
持ち物 敷物(バスタオルなど)
サイズ
A4
ページ数
両面
希望イメージ
シンプル 複雑
単色 カラフル
暗い 明るい
日常 高級
遊び心 厳粛
未来的 伝統的
女性的 男性的
希望する色
表紙は一円相(円の筆書き)を元になのでシックにですが、差し色を入れていただけるとありがたいです。

```html
<!DOCTYPE html>
<html lang="ja">
<head>
<meta charset="utf-8">
<title>静の語らい 第52回</title>
<link rel="stylesheet" href="https://fonts.googleapis.com/css2?family=Noto+Serif+JP:wght@400;600;700;900&family=Noto+Sans+JP:wght@400;500;700&display=swap">
<style>
:root{
  --leaf-deep:#7a1f10;
  --leaf-red:#b7321a;
  --leaf-orange:#d9702a;
  --leaf-gold:#e9a23b;
  --paper:#ffffff;
  --ink:#2a2624;
  --ink-soft:#5b5450;
  --accent:#c8321e;
  --label:#3b3432;
}
*{margin:0;padding:0;box-sizing:border-box}
html,body{width:848px;height:1200px;overflow:hidden}
body{font-family:"Noto Serif JP",serif;color:var(--ink)}
.flyer{position:relative;width:848px;height:1200px;overflow:hidden}
.leaf-backdrop{position:absolute;inset:0;
  background:
    radial-gradient(circle at 15% 10%,var(--leaf-gold) 0,transparent 30%),
    radial-gradient(circle at 85% 90%,var(--leaf-orange) 0,transparent 35%),
    radial-gradient(circle at 90% 20%,var(--leaf-red) 0,transparent 40%),
    linear-gradient(160deg,var(--leaf-orange),var(--leaf-red) 50%,var(--leaf-deep));}
.sheet{position:absolute;left:62px;top:52px;width:726px;height:1096px;background:var(--paper);overflow:hidden}
.ensou-art{position:absolute;left:0;top:0;width:726px;height:1096px}
.themes{position:absolute;left:122px;top:190px;font-family:"Noto Sans JP",sans-serif;font-weight:700;font-size:30px;line-height:42px;letter-spacing:3px}
.themes .cross{color:var(--accent);font-weight:400;font-size:40px;margin-left:6px;vertical-align:-3px}
.organizer{position:absolute;left:122px;top:518px;font-family:"Noto Sans JP",sans-serif;font-weight:700;font-size:16px;line-height:29px}
.organizer .edition{font-size:21px}
.title{position:absolute;left:118px;top:660px;font-weight:900;font-size:64px;line-height:1;letter-spacing:6px}
.subtitle{position:absolute;left:122px;top:740px;font-weight:700;font-size:25px;line-height:32px;letter-spacing:6px}
.speakers{position:absolute;left:190px;top:812px;display:flex;gap:34px}
.speaker{display:flex;align-items:flex-end;gap:10px}
.speaker-photo{width:62px;height:66px;background:linear-gradient(#bdb8b4,#8d8782)}
.speaker-role{font-family:"Noto Sans JP",sans-serif;font-size:10px;line-height:14px;color:var(--ink-soft)}
.speaker-name{font-size:17px;font-weight:700;letter-spacing:3px}
.schedule{position:absolute;left:122px;top:898px;font-family:"Noto Sans JP",sans-serif;font-weight:500}
.schedule .date{font-size:28px;line-height:38px}
.schedule .time{font-size:26px;line-height:38px}
.schedule .venue{font-family:"Noto Serif JP",serif;font-weight:700;font-size:22px;line-height:40px}
.credits{position:absolute;left:122px;top:1030px;font-family:"Noto Sans JP",sans-serif;font-size:10px;line-height:30px}
.credits .label{display:inline-block;background:var(--label);color:#fff;padding:0 5px;line-height:16px;margin-right:8px}
</style>
</head>
<body>
<div class="flyer">
  <div class="leaf-backdrop" role="img" aria-label="紅葉した落ち葉が一面に広がる背景"></div>
  <div class="sheet">
    <svg class="ensou-art" viewBox="0 0 726 1096" aria-hidden="false">
      <defs>
        <radialGradient id="figure-tone" cx="50%" cy="45%" r="60%">
          <stop offset="0" stop-color="#e9a23b"/>
          <stop offset=".5" stop-color="#d9702a"/>
          <stop offset="1" stop-color="#b7321a"/>
        </radialGradient>
      </defs>
      <path class="ensou-stroke" d="M622 360 A190 190 0 1 1 540 290" fill="none" stroke="#b7321a" stroke-width="14" stroke-linecap="round" opacity=".85"/>
      <rect class="figure-area" x="420" y="150" width="240" height="470" rx="110" fill="url(#figure-tone)" role="img" aria-label="紅葉の葉で形づくられた、坐禅を組む人物のシルエット"/>
    </svg>

    <div class="themes" style="left:60px;top:138px">
      <div>ヨーガ<span class="cross">×</span></div>
      <div>マインドフルネス<span class="cross">×</span></div>
      <div>坐禅</div>
    </div>
    <div class="organizer" style="left:60px;top:466px">
      <div>愛知県</div>
      <div>東部明照宗</div>
      <div>若人会主催</div>
      <div class="edition">第52回</div>
    </div>
    <h1 class="title" style="left:56px;top:608px">静の語らい</h1>
    <div class="subtitle" style="left:60px;top:688px">
      <div>深い呼吸で身体と心を調える</div>
      <div>（調身 調息 調心）</div>
    </div>
    <div class="speakers" style="left:128px;top:760px">
      <div class="speaker">
        <div class="speaker-photo" role="img" aria-label="講師 堀越達也氏の写真"></div>
        <div><div class="speaker-role">古層のヨーガ<br>講師</div><div class="speaker-name">堀越達也氏</div></div>
      </div>
      <div class="speaker">
        <div class="speaker-photo" role="img" aria-label="講師 柴崎和久氏の写真"></div>
        <div><div class="speaker-role">マインドフルネス講座<br>講師</div><div class="speaker-name">柴崎和久氏</div></div>
      </div>
    </div>
    <div class="schedule" style="left:60px;top:846px">
      <div class="date">2023.11.18(Sat.)</div>
      <div class="time">13:30-16:30 (12:30 Open)</div>
      <div class="venue">@慶雲山 桂林院</div>
    </div>
    <div class="credits" style="left:60px;top:978px">
      <div><span class="label">主催</span>愛知県東部明照宗若人会</div>
      <div><span class="label">後援</span>大本山清涼寺／大本山妙光寺／明照宗本務庁／明照宗愛知県東部本務所／東海報知</div>
    </div>
  </div>
</div>
</body>
</html>
```